会社ロゴに沿ったクラシカルな中に、親しみやすい印象を与えられるようなデザインを希望しております。

グラフィック的なデザインよりはアンティークなイメージで、シンプルで重厚感があり、信頼感の与えられるイメージが希望です。
色味もロゴに沿った深い青紫、白、黒。
差し色を使用するなら派手ではないゴールドを使用したいです。

記載項目
[表]
会社ロゴ(TOVI )
肩書き (合同会社TOVI 代表)
名前  (桐原 早苗)(KIRIHARA SANAE)

電話番号(000-000-0000)
メールアドレス(○○○○○@○○○○.com)

記載する順番はデザインに合わせていただいて結構です。
横型のデザインを希望です。

電話番号、メールアドレスは記載するものを今検討中ですので、選考までにはお伝えできるようにいたします。

-----------------------------
[裏]
店舗ロゴ(NOVE EYELASH)
店舗名 (まつげエクステNOVE港町本通店)
電話番号 092-518-4097
住所   〒813-0057
福岡県福岡市中央区港町3-4-12ルミエール港町305

裏面の店舗情報は用紙全面への表記ではなく、今後数店舗開店した時に記載を増やしていきたいので配置を考慮していただけますと幸いです。
現在一店舗の表記となるため、質素にならないようなデザインを加えていただけると大変うれしく思います。

グレー系、紫系

```html
<!DOCTYPE html>
<html lang="ja">
<head>
<meta charset="utf-8">
<title>TOVI 名刺デザイン 表・裏</title>
<link rel="stylesheet" href="https://fonts.googleapis.com/css2?family=Noto+Serif+JP:wght@400;500;600&family=Cinzel:wght@500;600&family=Lato:wght@400&display=swap">
<style>
  :root{
    --board:#e6e6e6;
    --label:#555555;
    --card-front:#ffffff;
    --card-back:#2b2323;
    --ink:#222222;
    --ink-soft:#555555;
    --rule:#9a9a9a;
    --ornament-light:#bdbdbd;
    --ornament-mid:#8a8a8a;
    --back-ink:#e8e4e4;
    --back-soft:#bfb6b6;
    --back-ornament:#4a4040;
  }
  *{margin:0;padding:0;box-sizing:border-box}
  html,body{width:805px;height:1200px;overflow:hidden;background:var(--board)}
  body{position:relative;font-family:"Noto Serif JP",serif;color:var(--ink)}
  .side-label{position:absolute;left:54px;font-family:"Lato",sans-serif;font-size:17px;color:var(--label)}
  .side-label--front{top:68px}
  .side-label--back{top:622px}
  .card{position:absolute;left:48px;width:711px;height:436px;box-shadow:0 2px 6px rgba(0,0,0,.25);overflow:hidden}
  .card--front{top:115px;background:var(--card-front)}
  .card--back{top:679px;background:var(--card-back);color:var(--back-ink)}

  .ornament{position:absolute}
  .ornament--top{right:0;top:0;width:340px;height:210px;
    background:radial-gradient(ellipse at 85% 30%,var(--ornament-mid) 0%,var(--ornament-light) 35%,rgba(255,255,255,0) 72%)}
  .ornament--bottom{right:0;bottom:0;width:220px;height:120px;
    background:radial-gradient(ellipse at 90% 80%,var(--ornament-mid) 0%,var(--ornament-light) 40%,rgba(255,255,255,0) 75%)}

  .title{position:absolute;left:129px;top:142px;font-size:15px;letter-spacing:.05em}
  .name{position:absolute;left:129px;top:178px;font-size:30px;font-weight:500;letter-spacing:.12em}
  .name-rule{position:absolute;left:86px;top:226px;width:344px;height:1px;background:var(--rule)}
  .name-roman{position:absolute;left:129px;top:248px;font-family:"Lato",sans-serif;font-size:12px;color:var(--ink-soft);letter-spacing:.05em}
  .contact{position:absolute;left:129px;font-family:"Lato",sans-serif;font-size:14px;color:var(--ink-soft);display:flex;align-items:center;gap:6px}
  .contact--phone{top:278px}
  .contact--mail{top:306px}
  .contact svg{width:15px;height:15px}

  .brand-mark{position:absolute;left:300px;top:246px;width:84px;height:84px;border:2px solid var(--ink);border-radius:50%}
  .brand-name{position:absolute;left:398px;top:268px;font-family:"Cinzel",serif;font-weight:600;font-size:34px;letter-spacing:.04em;color:var(--ink)}

  .ornament--swirl{right:0;top:30px;width:360px;height:380px;
    background:radial-gradient(ellipse at 60% 45%,var(--back-ornament) 0%,rgba(43,35,35,0) 70%)}
  .shop-mark{position:absolute;left:58px;top:206px;width:10px;height:10px;border-radius:50%;background:var(--back-ink)}
  .shop-logo{position:absolute;left:76px;top:196px;font-family:"Cinzel",serif;font-weight:500;font-size:28px;letter-spacing:.06em;color:var(--back-ink)}
  .shop-divider{position:absolute;left:176px;top:176px;width:1px;height:90px;background:var(--back-soft)}
  .shop-info{position:absolute;left:190px;top:176px;line-height:1}
  .shop-name{font-size:15px;font-weight:600;letter-spacing:.05em;margin-bottom:14px}
  .shop-address,.shop-tel{font-size:11.5px;color:var(--back-soft);margin-bottom:12px}
</style>
</head>
<body>
  <p class="side-label side-label--front">Front</p>
  <section class="card card--front" aria-label="名刺 表面">
    <div class="ornament ornament--top" role="img" aria-label="アンティーク調の唐草模様の装飾"></div>
    <div class="ornament ornament--bottom" role="img" aria-label="アンティーク調の唐草模様の装飾"></div>
    <p class="title">合同会社TOVI 代表</p>
    <h1 class="name">桐原 早苗</h1>
    <div class="name-rule"></div>
    <p class="name-roman">Sanae Kirihara</p>
    <p class="contact contact--phone">
      <svg viewBox="0 0 16 16" aria-hidden="true"><rect width="16" height="16" rx="2" fill="#555"/><path d="M5 3.5h2l.8 2.4-1.2.9a6 6 0 0 0 2.6 2.6l.9-1.2 2.4.8v2c0 .6-.5 1-1 1A8 8 0 0 1 4 4.5c0-.5.4-1 1-1z" fill="#fff"/></svg>
      090-0000-0000
    </p>
    <p class="contact contact--mail">
      <svg viewBox="0 0 16 16" aria-hidden="true"><rect width="16" height="16" rx="2" fill="#555"/><rect x="3" y="4.5" width="10" height="7" fill="none" stroke="#fff"/><path d="M3 4.5l5 4 5-4" fill="none" stroke="#fff"/></svg>
      info@example.com
    </p>
    <div class="brand-mark" aria-hidden="true"></div>
    <p class="brand-name">TOVI</p>
  </section>

  <p class="side-label side-label--back">Back</p>
  <section class="card card--back" aria-label="名刺 裏面">
    <div class="ornament ornament--swirl" role="img" aria-label="淡い渦巻き曲線の装飾"></div>
    <div class="shop-mark" aria-hidden="true"></div>
    <p class="shop-logo">NOVE</p>
    <div class="shop-divider"></div>
    <div class="shop-info">
      <p class="shop-name">まつげエクステNOVE港町本通店</p>
      <p class="shop-address">〒813-0057 福岡県福岡市中央区港町3-4-12ルミエール港町305</p>
      <p class="shop-tel">Tel 092-518-4097</p>
    </div>
  </section>
</body>
</html>
```